Flyer Template

I need a flyer template for door knocking on properties. Text Boxes need to be editable, with a header and text body. Footer to be my info. Project to be stylized to match my real estate signs and logo art from past projects

```html
<!DOCTYPE html>
<html lang="en">
<head>
<meta charset="utf-8">
<title>Modern House For Sale – Castell Realty</title>
<link rel="stylesheet" href="https://fonts.googleapis.com/css2?family=Roboto:ital,wght@0,300;0,400;0,500;0,700;0,900;1,700;1,900&family=Roboto+Condensed:wght@400;700&display=swap">
<style>
  :root {
    --red: #e5262f;
    --ink: #111111;
    --panel-light: #d1d2d4;
    --panel-dark: #58585a;
    --frame: #e3e4e6;
    --white: #ffffff;
    --text: #1c1c1c;
    --hero-light: #c9cdc8;
    --hero-dark: #6f7a68;
  }
  * { margin: 0; padding: 0; box-sizing: border-box; }
  html, body { width: 927px; height: 1200px; overflow: hidden; background: var(--white); }
  body { font-family: "Roboto", Arial, sans-serif; color: var(--text); }
  .flyer { position: relative; width: 927px; height: 1200px; overflow: hidden; background: var(--white); }
  .shapes { position: absolute; inset: 0; }

  .title { position: absolute; left: 40px; top: 62px; width: 260px; text-align: right; line-height: 1; }
  .title-main { font-weight: 300; font-size: 37px; color: var(--ink); letter-spacing: -0.3px; }
  .title-sub { margin-top: 10px; font-size: 22px; font-weight: 700; font-style: italic; color: var(--ink); }
  .title-sub strong { font-style: normal; font-size: 32px; font-weight: 900; }

  .title-divider { position: absolute; left: 330px; top: 68px; width: 3px; height: 77px; background: var(--panel-light); }

  .price { position: absolute; left: 350px; top: 88px; font-family: "Roboto Condensed", "Arial Narrow", sans-serif; font-weight: 700; font-size: 54px; color: var(--red); line-height: 1; letter-spacing: -0.5px; }
  .price .currency { font-weight: 400; font-size: 26px; margin-right: 3px; }

  .brand { position: absolute; display: flex; flex-direction: column; align-items: center; text-align: center; }
  .brand-mark { background: var(--red); }
  .brand-name { font-weight: 900; color: var(--ink); line-height: 1.2; }
  .brand--header { left: 720px; top: 56px; width: 150px; }
  .brand--header .brand-mark { width: 56px; height: 56px; margin-bottom: 42px; }
  .brand--header .brand-name { font-size: 28px; }
  .brand--footer { left: 386px; top: 1056px; width: 88px; }
  .brand--footer .brand-mark { width: 34px; height: 34px; margin-bottom: 22px; }
  .brand--footer .brand-name { font-size: 14.5px; line-height: 1.3; }

  .size { position: absolute; left: 47px; top: 578px; color: var(--red); line-height: 1; }
  .size-num { font-size: 45px; font-weight: 400; }
  .size-unit { font-size: 30px; margin-left: 6px; }
  .headline { position: absolute; left: 48px; top: 632px; font-size: 22px; font-weight: 700; line-height: 27px; color: var(--ink); }

  .about { position: absolute; left: 46px; top: 750px; width: 240px; }
  .about-title { font-size: 20px; font-weight: 700; font-style: italic; color: var(--ink); margin-bottom: 6px; }
  .about-body { font-size: 16px; line-height: 20px; color: var(--ink); }

  .features { position: absolute; left: 51px; top: 945px; list-style: none; }
  .features li { font-size: 19px; font-weight: 700; color: var(--white); height: 37.2px; line-height: 26px; }

  .room { position: absolute; width: 227px; }
  .room-photo { display: block; width: 227px; height: 150px; }
  .room-caption { display: flex; align-items: center; gap: 9px; margin-top: 7px; font-size: 16px; color: var(--ink); white-space: nowrap; }
  .room-caption::after { content: ""; flex: 1; height: 1px; background: var(--red); }
  .room--living { left: 368px; top: 556px; }
  .room--bedroom { left: 618px; top: 556px; }
  .room--kitchen { left: 368px; top: 764px; }
  .room--bathroom { left: 618px; top: 764px; }
  .room--living .room-photo, .room--kitchen .room-photo { background: linear-gradient(135deg, #c8bcae 0%, #e4e2de 100%); }
  .room--bedroom .room-photo, .room--bathroom .room-photo { background: linear-gradient(135deg, #d4d8da 0%, #e9e8e5 100%); }

  .details { position: absolute; left: 505px; top: 947px; width: 345px; font-size: 14.6px; line-height: 18.2px; color: var(--ink); }

  .agent-name { position: absolute; right: 45px; top: 1128px; font-size: 19px; font-weight: 700; color: var(--red); }
  .footer-rule { position: absolute; left: 370px; top: 1156px; width: 512px; height: 1px; background: var(--red); }
  .office { position: absolute; left: 369px; top: 1163px; line-height: 1; }
  .office-name { font-family: "Roboto Condensed", "Arial Narrow", sans-serif; font-size: 16px; font-weight: 700; color: var(--panel-dark); letter-spacing: -0.3px; }
  .office-sub { font-family: "Roboto Condensed", "Arial Narrow", sans-serif; font-size: 6.5px; color: var(--panel-dark); margin-top: 2px; letter-spacing: 0.2px; }
  .contact { position: absolute; top: 1165px; display: flex; align-items: center; gap: 5px; font-size: 14px; color: var(--ink); }
  .contact svg { width: 12px; height: 12px; fill: #9a9b9d; }
  .contact--phone { left: 602px; }
  .contact--email { right: 43px; }
</style>
</head>
<body>
<main class="flyer">
  <svg class="shapes" width="927" height="1200" viewBox="0 0 927 1200">
    <defs>
      <linearGradient id="heroTones" x1="0" y1="0" x2="1" y2="1">
        <stop offset="0" stop-color="var(--hero-dark)"/>
        <stop offset="1" stop-color="var(--hero-light)"/>
      </linearGradient>
    </defs>
    <polyline class="frame-line" points="306,0 331,36 513,36 881,402 881,485 847,485" fill="none" stroke="var(--frame)" stroke-width="1.5"/>
    <polygon class="hero-accent" points="828,423 847,442 847,531 0,531 0,510 828,510" fill="var(--red)"/>
    <polygon class="hero-photo" role="img" aria-label="Exterior photo of a two-storey modern white stucco house with dark tiled hip roofs, stone entry and landscaped lawn, set among tall trees" points="0,159 593,159 828,392 828,510 0,510" fill="url(#heroTones)"/>
    <polygon class="about-panel" points="0,727 266,727 332,793 332,913 0,913" fill="var(--panel-light)"/>
    <rect class="features-panel" x="0" y="913" width="332" height="287" fill="var(--panel-dark)"/>
  </svg>

  <header>
    <div class="title">
      <div class="title-main">Modern House</div>
      <div class="title-sub">FOR <strong>SALE</strong></div>
    </div>
    <div class="title-divider"></div>
    <div class="price"><span class="currency">$</span>1,00,000</div>
    <div class="brand brand--header">
      <span class="brand-mark"></span>
      <span class="brand-name">CASTELL<br>REALTY</span>
    </div>
  </header>

  <section>
    <div class="size"><span class="size-num">2000</span><span class="size-unit">Sq. Mtr.</span></div>
    <h2 class="headline">Luxury Villa in<br>Southern County</h2>

    <div class="about">
      <h3 class="about-title">About Property</h3>
      <p class="about-body">Lorem ipsum dolor sit amet, consectetuer adipiscing elit, sed diam nonummy nibh euismod tincidunt ut laoreet dolore magna aliquam erat volutpat. Ut wisi enim ad minim veniam,</p>
    </div>

    <ul class="features">
      <li>Living Room</li>
      <li>Dining Room</li>
      <li>2 Bedroom</li>
      <li>Swimming Pool</li>
      <li>Storage Room</li>
      <li>Garden</li>
    </ul>
  </section>

  <section class="gallery">
    <figure class="room room--living">
      <div class="room-photo" role="img" aria-label="Bright living room with sliding glass doors, white sofas, blue cushions and a dark rug"></div>
      <figcaption class="room-caption">Living Room</figcaption>
    </figure>
    <figure class="room room--bedroom">
      <div class="room-photo" role="img" aria-label="Light room with large window, freestanding tub and white vanity"></div>
      <figcaption class="room-caption">Bedroom</figcaption>
    </figure>
    <figure class="room room--kitchen">
      <div class="room-photo" role="img" aria-label="Open-plan interior with white kitchen behind seating area and patio doors"></div>
      <figcaption class="room-caption">Kitchen</figcaption>
    </figure>
    <figure class="room room--bathroom">
      <div class="room-photo" role="img" aria-label="Bathroom with freestanding tub, window and white vanity with mirror"></div>
      <figcaption class="room-caption">Bathroom</figcaption>
    </figure>
  </section>

  <p class="details">Lorem ipsum dolor sit amet, consectetuer adipiscing elit, sed diam nonummy nibh euismod tincidunt Lorem ipsum dolor sit amet, consectetuer adipiscing elit, sed diam nonummy nibh euismod tincidunt ut laoreet dolore magna aliquam erat volutpat. Ut wisi enim ad minim veniam, quis nostrud exerci</p>

  <footer>
    <div class="brand brand--footer">
      <span class="brand-mark"></span>
      <span class="brand-name">CASTELL<br>REALTY</span>
    </div>
    <div class="agent-name">Jordan Castell</div>
    <div class="footer-rule"></div>
    <div class="office">
      <div class="office-name">NORTHWAY GROUP</div>
      <div class="office-sub">NORTHWAY REALTY</div>
    </div>
    <div class="contact contact--phone">
      <svg viewBox="0 0 24 24"><rect x="0" y="0" width="24" height="24" rx="4"/><path d="M8 5c1 0 2 2.5 2 3.2 0 .8-1.2 1.2-1 2 .5 1.6 2.2 3.3 3.8 3.8.8.2 1.2-1 2-1 .7 0 3.2 1 3.2 2 0 1.6-1.5 3-3 3C9.5 18 6 14.5 6 9.5 6 7 7 5 8 5z" fill="#fff"/></svg>
      <span>555-010-2288</span>
    </div>
    <div class="contact contact--email">
      <svg viewBox="0 0 24 18" style="width:15px"><rect x="0" y="0" width="24" height="18" rx="2"/><path d="M2 2l10 8 10-8" fill="none" stroke="#fff" stroke-width="2"/></svg>
      <span>jcastell@example.com</span>
    </div>
  </footer>
</main>
</body>
</html>
```